Flyer Design Project

We are offering a new class on cyber crime and want to advertise this course to students. We would like to see a design that is eye catching and coveys the goals of the course, when it meets and a brief abstract for the class.

The course will focus on the economics of cyber crime so including one or two graphics that get across this point would be good.

Requirements
Must have
• Course name "Cyber Crime"
Call number "CS 795 - 004"
Course meeting time (day of week and time) Tue. 4:30-7:10pm
Course goals
Course abstract

```html
<!DOCTYPE html>
<html lang="en">
<head>
<meta charset="utf-8">
<title>Cyber Crime – Course Flyer</title>
<link rel="stylesheet" href="https://fonts.googleapis.com/css2?family=Archivo+Black&family=Arimo:wght@400;700&family=Didact+Gothic&display=swap">
<style>
  :root {
    --ink: #000000;
    --paper: #ffffff;
    --panel-yellow: #ffee00;
    --panel-orange: #f7941d;
    --hero-deep: #020b24;
    --hero-mid: #0a3d8f;
    --hero-glow: #7fd3ff;
    --title-fill-top: #fff200;
    --title-fill-bottom: #f7941d;
    --title-stroke: #e2231a;
    --chart-bar: #f7941d;
    --chart-line: #ffee00;
    --chart-axis: #8a8a8a;
  }
  * { margin: 0; padding: 0; box-sizing: border-box; }
  html, body { width: 927px; height: 1200px; overflow: hidden; background: var(--paper); }
  .flyer {
    position: relative;
    width: 927px;
    height: 1200px;
    background: var(--ink);
    font-family: "Didact Gothic", "Century Gothic", sans-serif;
    color: var(--ink);
  }
  .hero {
    position: absolute;
    left: 0; top: 0;
    width: 927px; height: 535px;
    background:
      radial-gradient(ellipse 40% 30% at 50% 32%, var(--hero-glow) 0%, rgba(40,120,220,0.55) 40%, transparent 75%),
      radial-gradient(ellipse 90% 60% at 50% 70%, var(--hero-mid) 0%, var(--hero-deep) 80%);
  }
  .course-title {
    position: absolute;
    left: 0; top: 70px;
    width: 927px; height: 180px;
  }
  .info-panel {
    position: absolute;
    left: 0; top: 535px;
    width: 580px; height: 606px;
    background: linear-gradient(90deg, var(--panel-yellow) 0%, var(--panel-orange) 100%);
  }
  .section-heading {
    font-family: "Arimo", Arial, sans-serif;
    font-weight: 700;
    font-size: 23px;
    line-height: 1;
  }
  .info-panel .section-heading,
  .info-panel .body-copy { position: absolute; left: 71px; width: 486px; }
  .goal-heading { top: 30px; }
  .goal-one { top: 70px; }
  .goal-two { top: 136px; }
  .abstract-heading { top: 240px; }
  .abstract-text { top: 277px; }
  .body-copy {
    font-size: 18.5px;
    line-height: 23.8px;
  }
  .body-copy .line {
    display: block;
    white-space: nowrap;
    text-align: justify;
    text-align-last: justify;
  }
  .body-copy .line.end { text-align-last: left; }
  .details {
    position: absolute;
    left: 608px; top: 565px;
    width: 300px;
    color: var(--paper);
  }
  .details .section-heading { margin-bottom: 14px; }
  .details p {
    font-family: "Arimo", Arial, sans-serif;
    font-size: 14.5px;
    line-height: 22px;
    margin-bottom: 26px;
  }
  .economics-chart {
    position: absolute;
    left: 620px; top: 800px;
    width: 270px; height: 220px;
  }
  .course-link {
    position: absolute;
    left: 61px; top: 1157px;
    font-family: "Arimo", Arial, sans-serif;
    font-weight: 700;
    font-size: 23px;
    color: var(--paper);
  }
</style>
</head>
<body>
<main class="flyer">
  <div class="hero" role="img" aria-label="Glowing blue digital scene of computer monitors with hands reaching out toward keyboards, over streams of binary code"></div>

  <svg class="course-title" viewBox="0 0 927 180" aria-label="Cyber Crime">
    <defs>
      <linearGradient id="titleFill" x1="0" y1="0" x2="0" y2="1">
        <stop offset="0" stop-color="var(--title-fill-top)"/>
        <stop offset="1" stop-color="var(--title-fill-bottom)"/>
      </linearGradient>
    </defs>
    <text x="463" y="150" text-anchor="middle" textLength="730" lengthAdjust="spacingAndGlyphs"
          font-family="Archivo Black, Arial Black, sans-serif" font-size="150"
          fill="url(#titleFill)" stroke="var(--title-stroke)" stroke-width="6" paint-order="stroke">Cyber Crime</text>
  </svg>

  <section class="info-panel">
    <h2 class="section-heading goal-heading">The Goal of the Class:</h2>
    <p class="body-copy goal-one">
      <span class="line">1) Understand how modern cyber-crime</span>
      <span class="line end">operates on a technical and economic level.</span>
    </p>
    <p class="body-copy goal-two">
      <span class="line">2) Analyze some of the potential places to</span>
      <span class="line">intervene at an economic, technical and policy</span>
      <span class="line end">level.</span>
    </p>
    <h2 class="section-heading abstract-heading">Course Abstract:</h2>
    <p class="body-copy abstract-text">
      <span class="line">Arguably the single most significant change in</span>
      <span class="line">the cyber-security landscape has been the</span>
      <span class="line">explosive rise of profit-fueled cyber-crime.</span>
      <span class="line">Obtaining a detailed, structural understanding</span>
      <span class="line">of how profit-driven cyber crime works — its</span>
      <span class="line">underlying economics and associated business</span>
      <span class="line">practices — has the potential to illuminate new</span>
      <span class="line">defensive measures that might prove far more</span>
      <span class="line">efficient for countering attacks than purely</span>
      <span class="line">technical measures. This research seminar will</span>
      <span class="line">delve into our current understanding of the</span>
      <span class="line end">economics of cyber-crime.</span>
    </p>
  </section>

  <aside class="details">
    <h2 class="section-heading">Course Number:</h2>
    <p>CS 795 - 004</p>
    <h2 class="section-heading">Course Meeting Time:</h2>
    <p>Fall 2012<br>(day of week and time)<br>Tue. 4:30-7:10pm</p>
  </aside>

  <svg class="economics-chart" viewBox="0 0 270 220" role="img" aria-label="Bar chart of rising profits from cyber-crime">
    <line x1="10" y1="200" x2="260" y2="200" stroke="var(--chart-axis)" stroke-width="2"/>
    <line x1="10" y1="200" x2="10" y2="10" stroke="var(--chart-axis)" stroke-width="2"/>
    <rect x="30" y="160" width="32" height="40" fill="var(--chart-bar)"/>
    <rect x="78" y="130" width="32" height="70" fill="var(--chart-bar)"/>
    <rect x="126" y="100" width="32" height="100" fill="var(--chart-bar)"/>
    <rect x="174" y="70" width="32" height="130" fill="var(--chart-bar)"/>
    <rect x="222" y="30" width="32" height="170" fill="var(--chart-bar)"/>
    <polyline points="46,145 94,115 142,85 190,55 238,18" fill="none" stroke="var(--chart-line)" stroke-width="4" stroke-linejoin="round"/>
    <polygon points="238,8 248,24 230,24" fill="var(--chart-line)"/>
  </svg>

  <p class="course-link">http://cs.northfield.edu/~lindqvist/crime.html</p>
</main>
</body>
</html>
```